Description of Adventure Certificate:
We require a certificate, that will be awarded to winners of competitions and offered to fundraising organisations for a $ value or type of event service we provide.
The certificate will be professionally printed on thick high-quality paper.
Design concept: Adventurous outer border, and exciting theme.
Title: Adventure Certificate (adventurous font)
Content: "Bringing the Thrill of Adventure to you"
Awarded To:..........................................
From:....................................................
Amount / Event: ...................................
Redemption Location:...........................
Expires:.................................................
Events listed near the base of certificate: Community events, Sports celebrations, Team building, School activities, Festivals, Vacation Care, EXPO's, Trade Shows.
Contact: M: 0418 627 349
E: info@tidalkite.com.au
Images: Tidal Kite Logo
Adventure Certificate image
Carabiner

```html
<!DOCTYPE html>
<html lang="en">
<head>
<meta charset="utf-8">
<title>Tidal Kite – Adventure Certificate</title>
<link href="https://fonts.googleapis.com/css2?family=Lato:wght@400;700&family=Permanent+Marker&family=Caveat+Brush&display=swap" rel="stylesheet">
<style>
  :root {
    --page-bg: #ecebe8;
    --sky-light: #dfeaf6;
    --sky-mid: #a9c6e6;
    --sky-deep: #6f9fd4;
    --rock: #9a3b22;
    --rock-dark: #5e2413;
    --accent: #e8532c;
    --accent-deep: #c8401f;
    --ink: #1c1c1c;
    --rule: #2a2a2a;
    --icon-tan: #c9a77a;
    --icon-red: #d0463a;
    --icon-navy: #2e3f78;
    --icon-sage: #9fb58e;
  }
  * { box-sizing: border-box; margin: 0; padding: 0; }
  html, body { width: 1200px; height: 1000px; overflow: hidden; background: var(--page-bg); }
  .certificate {
    position: absolute; left: 20px; top: 80px; width: 1160px; height: 840px;
    background: linear-gradient(100deg, var(--sky-mid) 0%, var(--sky-light) 45%, #f7f9fc 100%);
    font-family: "Lato", sans-serif; color: var(--ink); overflow: hidden;
  }
  .hero-photo {
    position: absolute; left: 0; top: 0; width: 440px; height: 840px;
    background: linear-gradient(180deg, var(--sky-deep) 0%, var(--sky-mid) 20%, #b8866f 30%, var(--rock) 45%, var(--rock-dark) 100%);
  }
  .brand { position: absolute; left: 56px; top: 40px; display: flex; align-items: center; gap: 12px; }
  .brand-dot { width: 50px; height: 50px; border-radius: 50%; background: var(--accent); }
  .brand-name { font-weight: 700; font-size: 40px; color: var(--ink); }

  .icon-border { position: absolute; border-radius: 6px; opacity: .9; }
  .icon-border--top {
    left: 476px; top: 18px; width: 640px; height: 26px;
    background: linear-gradient(90deg, var(--icon-tan), var(--icon-red) 25%, var(--icon-sage) 50%, var(--icon-navy) 75%, var(--icon-tan));
  }
  .icon-border--right {
    left: 1118px; top: 18px; width: 26px; height: 806px;
    background: linear-gradient(180deg, var(--icon-sage), var(--icon-navy) 20%, var(--icon-tan) 40%, var(--icon-red) 60%, var(--icon-sage) 80%, var(--icon-navy));
  }
  .icon-border--bottom {
    left: 456px; top: 798px; width: 660px; height: 26px;
    background: linear-gradient(90deg, var(--icon-red), var(--icon-tan) 25%, var(--icon-navy) 50%, var(--icon-sage) 75%, var(--icon-red));
  }

  .title-block { position: absolute; left: 532px; top: 112px; width: 560px; }
  .title {
    font-family: "Permanent Marker", "Caveat Brush", "Marker Felt", "Comic Sans MS", cursive;
    font-weight: 400; font-size: 44px; line-height: 1.1; color: var(--accent);
    letter-spacing: 1px; text-transform: uppercase; text-shadow: 1px 1px 0 var(--accent-deep);
    white-space: nowrap;
  }
  .tagline {
    font-family: "Permanent Marker", "Caveat Brush", "Marker Felt", "Comic Sans MS", cursive;
    font-size: 18px; color: var(--ink); text-transform: uppercase; letter-spacing: 1.5px;
    margin-top: 6px; white-space: nowrap;
  }

  .fields { position: absolute; left: 480px; top: 290px; width: 600px; list-style: none; }
  .field { display: flex; align-items: flex-end; height: 64px; }
  .field-label { font-size: 30px; color: var(--accent); white-space: nowrap; margin-right: 14px; }
  .field-line { flex: 1; border-bottom: 2px solid var(--rule); margin-bottom: 6px; }

  .signature { position: absolute; left: 800px; top: 680px; width: 270px; text-align: center; }
  .signature-line { border-top: 2px solid var(--rule); }
  .signature-label { font-size: 22px; margin-top: 8px; }

  .contacts { position: absolute; left: 540px; top: 748px; display: flex; gap: 70px; font-size: 19px; font-weight: 700; }
  .contact { display: flex; align-items: center; gap: 8px; white-space: nowrap; }
  .contact svg { width: 18px; height: 18px; }
</style>
</head>
<body>
  <main class="certificate">
    <div class="hero-photo" role="img" aria-label="Photo of children climbing a tall red rock climbing tower against a blue sky"></div>
    <div class="brand">
      <span class="brand-dot"></span>
      <span class="brand-name">Tidal Kite</span>
    </div>

    <div class="icon-border icon-border--top" role="img" aria-label="Border row of small adventure icons: ship wheels, tents, pirate flags, carabiners, maps, compasses, anchors"></div>
    <div class="icon-border icon-border--right" role="img" aria-label="Border column of small adventure icons: maps, compasses, anchors, ship wheels, tents, pirate flags, carabiners"></div>
    <div class="icon-border icon-border--bottom" role="img" aria-label="Border row of small adventure icons: carabiners, pirate flags, tents, ship wheels, anchors, compasses, maps"></div>

    <header class="title-block">
      <h1 class="title">Adventure Certificate</h1>
      <p class="tagline">Bringing the Thrill of Adventure to You</p>
    </header>

    <ul class="fields">
      <li class="field"><span class="field-label">Awarded To:</span><span class="field-line"></span></li>
      <li class="field"><span class="field-label">From:</span><span class="field-line"></span></li>
      <li class="field"><span class="field-label">Amount / Event:</span><span class="field-line"></span></li>
      <li class="field"><span class="field-label">Redemption Location:</span><span class="field-line"></span></li>
      <li class="field"><span class="field-label">Expires:</span><span class="field-line"></span></li>
    </ul>

    <div class="signature">
      <div class="signature-line"></div>
      <p class="signature-label">Signature</p>
    </div>

    <div class="contacts">
      <span class="contact">
        <svg viewBox="0 0 20 20" aria-hidden="true"><circle cx="10" cy="10" r="8.5" fill="none" stroke="#e8532c" stroke-width="1.6"/><path d="M7 5.5l2 2-1 1.2c.6 1.3 1.5 2.2 2.8 2.8l1.2-1 2 2-1.2 1.5c-3.2-.4-6.4-3.6-6.8-6.8z" fill="#e8532c"/></svg>
        0418 627 349
      </span>
      <span class="contact">
        <svg viewBox="0 0 20 20" aria-hidden="true"><rect x="2" y="4.5" width="16" height="11" fill="none" stroke="#e8532c" stroke-width="1.6"/><path d="M2 4.5l8 6.5 8-6.5" fill="none" stroke="#e8532c" stroke-width="1.6"/></svg>
        info@tidalkite.com.au
      </span>
    </div>
  </main>
</body>
</html>
```